I need a creative wine label design for my brand called BIM BAM. A design that catches the eye of the millennial consumer! Something very creative and playing off of the BIM BAM concept.

This will be a Red Blend 2019 vintage from California

Target Market(s)

Millennial wine consumer

Requirements
Must have
• Must have a design that attracts the millennial wine consumer. This must have creative flare.
Should not have
• Nothing corny!

```html
<!DOCTYPE html>
<html lang="en">
<head>
<meta charset="utf-8">
<title>BIM BAM — Red Blend 2019 Label</title>
<link rel="stylesheet" href="https://fonts.googleapis.com/css2?family=Playfair+Display:wght@700;900&family=PT+Sans&family=Libre+Baskerville&display=swap">
<style>
  :root {
    --backdrop: #1b1b1b;
    --label: #0d0d0d;
    --silver: #dcdcdc;
    --red: #d0101c;
    --grey: #5d5d5d;
    --text-light: #cfcfcf;
    --map-red: #5a0a0f;
  }
  * { margin: 0; padding: 0; box-sizing: border-box; }
  html, body {
    width: 1200px;
    height: 959px;
    overflow: hidden;
    background: var(--backdrop);
  }
  .canvas {
    position: relative;
    width: 1200px;
    height: 959px;
  }
  .label {
    position: absolute;
    left: 340px;
    top: 30px;
    width: 520px;
    height: 900px;
    background: var(--label);
  }
  .wordmark {
    position: absolute;
    left: 0;
    top: 88px;
    width: 100%;
    text-align: center;
    font-family: "Playfair Display", serif;
    font-weight: 900;
    font-size: 150px;
    line-height: 136px;
    letter-spacing: -2px;
    color: var(--silver);
  }
  .region-map {
    position: absolute;
    left: 185px;
    top: 419px;
    width: 150px;
    height: 228px;
  }
  .origin {
    position: absolute;
    left: 0;
    width: 100%;
    text-align: center;
    font-family: "PT Sans", sans-serif;
    color: var(--text-light);
  }
  .origin-kicker {
    top: 514px;
    font-size: 19px;
    letter-spacing: 8px;
  }
  .origin-rule {
    position: absolute;
    top: 526px;
    width: 12px;
    height: 1px;
    background: var(--grey);
  }
  .origin-rule.left { left: 78px; }
  .origin-rule.right { right: 78px; }
  .origin-state {
    top: 555px;
    font-size: 30px;
    letter-spacing: 15px;
    padding-left: 15px;
  }
  .varietal {
    position: absolute;
    left: 0;
    top: 688px;
    width: 100%;
    text-align: center;
    font-family: "Playfair Display", serif;
    font-weight: 700;
    font-size: 32px;
    letter-spacing: 9px;
    color: var(--red);
  }
  .vintage {
    position: absolute;
    left: 0;
    top: 738px;
    width: 100%;
    text-align: center;
    font-family: "Playfair Display", serif;
    font-weight: 700;
    font-size: 40px;
    letter-spacing: 9px;
    color: var(--grey);
  }
  .volume {
    position: absolute;
    left: 0;
    top: 832px;
    width: 100%;
    text-align: center;
    font-family: "Libre Baskerville", serif;
    font-size: 18px;
    letter-spacing: 1px;
    color: var(--text-light);
    word-spacing: 3px;
  }
</style>
</head>
<body>
  <main class="canvas">
    <section class="label">
      <h1 class="wordmark">BIM<br>BAM</h1>

      <svg class="region-map" viewBox="0 0 150 228" role="img" aria-label="Outline map of California">
        <defs>
          <radialGradient id="mapTone" cx="50%" cy="50%" r="60%">
            <stop offset="0%" stop-color="#5a0a0f" stop-opacity="0.55"/>
            <stop offset="100%" stop-color="#5a0a0f" stop-opacity="0"/>
          </radialGradient>
        </defs>
        <rect width="150" height="228" fill="url(#mapTone)"/>
      </svg>

      <span class="origin-rule left"></span>
      <span class="origin-rule right"></span>
      <p class="origin origin-kicker">VINTAGE FROM</p>
      <p class="origin origin-state">CALIFORNIA</p>

      <p class="varietal">RED BLEND</p>
      <p class="vintage">2019</p>

      <p class="volume">750 ml &nbsp;|&nbsp; 13% vol.</p>
    </section>
  </main>
</body>
</html>
```